40-year-old commercial construction firm :: Business Card Revamp

We are a 40 year-old, private general construction company based in Dallas, Texas, and we are considering updating our business cards, which could lead to a larger "brand refresh" campaign.

We work in a competitive environment, selling to business owners and executives making large scale purchasing decisions on behalf of their firms. A majority of our business is repeat business, with a long sales-cycle; while business can be difficult to identify and land, the effort is often rewarded with multiple projects.

We are open to a logo "refresh" as well as designs that incorporate the existing logo.

Target Market(s)

B2B selling to business owners/executives/end users who make facility decisions for their firms.

Industry/Entity Type

Construction Company

Contact Information for Business Card

Refresh from the example provided

Logo Text

Harkel Building Company :: See card example

Font styles to use
Other font styles liked:
• See sample card :: Designers to choose

Colors

Designer to choose colors to be used in the design.

Requirements
Must have
• Design should convey:
• Confidence
• Competence
• Capability
• Stability
• Tagline: Genuine Relationships :: Superior Services :: Environmentally Aware
Nice to have
• A solid design that is transferable from print to online.
• Note that we are also considering a painted-edge printing / card design
Should not have
• Too much color or whimsy. Our clients tend to be the serious type, and we work hard to present a serious, professional presence in the marketplace.

```html
<!DOCTYPE html>
<html lang="en">
<head>
<meta charset="UTF-8">
<title>Harkel Building Company – Business Card</title>
<link rel="stylesheet" href="https://fonts.googleapis.com/css2?family=Open+Sans:wght@400;600&family=Work+Sans:wght@300;400;500&display=swap">
<style>
  :root {
    --backdrop: #2a2928;
    --card: #ffffff;
    --gold: #c4a01e;
    --ink: #1b1b1b;
    --muted: #2e2e2e;
  }
  * { box-sizing: border-box; margin: 0; padding: 0; }
  html, body { width: 1200px; height: 930px; overflow: hidden; }
  body {
    background: var(--backdrop);
    position: relative;
    font-family: "Work Sans", Arial, sans-serif;
  }
  .card {
    position: absolute;
    top: 293px;
    width: 540px;
    height: 309px;
    background: var(--card);
    border-radius: 18px;
    overflow: hidden;
  }
  .card--front { left: 42px; }
  .card--back { left: 612px; }

  .edge-mark {
    position: absolute;
    top: 0;
    height: 309px;
    width: 160px;
  }
  .card--front .edge-mark { right: 0; }
  .card--back .edge-mark { left: 0; }
  .edge-mark ellipse { fill: none; stroke: var(--gold); stroke-width: 26; }

  .wordmark {
    position: absolute;
    display: flex;
    align-items: center;
    gap: 10px;
    font-family: "Open Sans", Arial, sans-serif;
    font-weight: 600;
    color: var(--ink);
    white-space: nowrap;
  }
  .wordmark__dot {
    display: block;
    border-radius: 50%;
    background: var(--gold);
    flex: none;
  }
  .card--front .wordmark { left: 28px; top: 44px; font-size: 21px; }
  .card--front .wordmark__dot { width: 42px; height: 42px; }
  .card--back .wordmark { right: 58px; top: 120px; font-size: 27px; }
  .card--back .wordmark__dot { width: 54px; height: 54px; }

  .tagline {
    position: absolute;
    right: 58px;
    top: 186px;
    text-align: right;
    font-weight: 400;
    font-size: 11px;
    line-height: 16px;
    letter-spacing: 0.6px;
    color: var(--gold);
  }

  .person { position: absolute; left: 29px; top: 130px; }
  .person__name {
    font-weight: 500;
    font-size: 25px;
    letter-spacing: 1.5px;
    color: var(--gold);
    line-height: 1;
  }
  .person__role {
    margin-top: 6px;
    font-weight: 300;
    font-size: 14px;
    color: var(--muted);
  }
  .address {
    position: absolute;
    left: 29px;
    top: 176px;
    font-style: normal;
    font-weight: 300;
    font-size: 14px;
    line-height: 18px;
    color: var(--muted);
  }
  .contacts {
    position: absolute;
    left: 29px;
    top: 219px;
    list-style: none;
    font-weight: 300;
    font-size: 14px;
    line-height: 17px;
    color: var(--muted);
  }
  .contacts li { display: flex; align-items: center; gap: 10px; }
  .contacts svg { width: 8px; height: 8px; fill: var(--gold); flex: none; }
</style>
</head>
<body>
  <section class="card card--front" aria-label="Business card front">
    <svg class="edge-mark" viewBox="0 0 160 309" role="img" aria-label="Large gold brand ring running off the card edge">
      <ellipse cx="175" cy="154" rx="150" ry="160"/>
    </svg>
    <div class="wordmark"><span class="wordmark__dot"></span>Harkel Building Company</div>
    <div class="person">
      <h1 class="person__name">MAREK OLSEN</h1>
      <p class="person__role">Director</p>
    </div>
    <address class="address">42 Meridian Park Drive,<br>Suite 210, Garland, TX</address>
    <ul class="contacts">
      <li><svg viewBox="0 0 8 8"><rect x="1.5" y="0" width="5" height="8" rx="1"/></svg>+45 20 38 51 00</li>
      <li><svg viewBox="0 0 8 8"><path d="M1 0h2l1 2-1 1a5 5 0 0 0 2 2l1-1 2 1v2c0 .6-.4 1-1 1A7 7 0 0 1 0 1c0-.6.4-1 1-1z"/></svg>+45 20 38 52 00</li>
      <li><svg viewBox="0 0 8 8"><path d="M0 1.5h8v5H0z M0 1.5l4 3 4-3" fill="none" stroke="#c4a01e" stroke-width="1"/></svg>info@harkelbuilding.com</li>
      <li><svg viewBox="0 0 8 8"><circle cx="4" cy="4" r="3.5" fill="none" stroke="#c4a01e" stroke-width="1"/><path d="M0.5 4h7M4 .5v7" stroke="#c4a01e" stroke-width="0.8"/></svg>www.harkelbuilding.com</li>
    </ul>
  </section>

  <section class="card card--back" aria-label="Business card back">
    <svg class="edge-mark" viewBox="0 0 160 309" role="img" aria-label="Large gold brand ring continuing from the front card">
      <ellipse cx="-15" cy="154" rx="150" ry="160"/>
    </svg>
    <div class="wordmark"><span class="wordmark__dot"></span>Harkel Building Company</div>
    <p class="tagline">Genuine Relationships :: Superior Services<br>:: Environmentally Aware</p>
  </section>
</body>
</html>
```